Moravel Stenwick Inc needs a business card design

Looking for a unique, classy and sharp business card design.

Contact Information for Business Card

Moravel Stenwick Inc.
Marisa Ortega Bellido BScOT(c)
Occupational Therapist
(780) 555-0142
moravelstenwick@postlynx.net

```html
<!DOCTYPE html>
<html lang="en">
<head>
<meta charset="utf-8">
<title>Moravel Stenwick Inc. — Business Card</title>
<link href="https://fonts.googleapis.com/css2?family=Montserrat:wght@400;600;700&display=swap" rel="stylesheet">
<style>
  :root {
    --backdrop: #eef1ea;
    --card: #fbfbf9;
    --card-edge: #c8423a;
    --brand-purple: #7a3d8f;
    --brand-green: #8cc152;
    --ink: #3c3c3c;
    --ink-soft: #6a6a6a;
    --leaf-tint: #e3ecd9;
  }
  * { box-sizing: border-box; margin: 0; padding: 0; }
  html, body {
    width: 1200px; height: 958px; overflow: hidden;
    background: var(--backdrop);
    font-family: "Montserrat", sans-serif;
  }
  .stage {
    width: 1200px; height: 958px;
    display: flex; align-items: center; justify-content: center;
  }
  .business-card {
    position: relative;
    width: 840px; height: 480px;
    background: var(--card);
    border-bottom: 4px solid var(--card-edge);
    box-shadow: 0 18px 40px rgba(0,0,0,0.12);
    overflow: hidden;
  }
  .leaf-pattern {
    position: absolute;
    left: 0; bottom: 0;
    width: 560px; height: 300px;
    background: radial-gradient(ellipse at 30% 70%, var(--leaf-tint) 0%, rgba(227,236,217,0.5) 45%, rgba(251,251,249,0) 75%);
  }
  .brand {
    position: absolute;
    top: 70px; right: 70px;
    display: flex; align-items: center; gap: 14px;
  }
  .brand-dot {
    width: 34px; height: 34px; border-radius: 50%;
    background: var(--brand-green);
  }
  .brand-name {
    font-weight: 700; font-size: 34px;
    color: var(--brand-purple);
    letter-spacing: -0.5px;
  }
  .identity {
    position: absolute;
    top: 170px; right: 70px;
    text-align: right;
  }
  .person-name {
    font-weight: 700; font-size: 22px; color: var(--ink);
  }
  .person-role {
    margin-top: 6px;
    font-weight: 400; font-size: 19px; color: var(--ink-soft);
  }
  .contact {
    position: absolute;
    left: 60px; bottom: 60px;
    list-style: none;
    font-size: 16px; color: var(--ink);
  }
  .contact li {
    display: flex; align-items: center; gap: 10px;
    margin-top: 8px;
  }
  .contact svg { width: 16px; height: 16px; fill: var(--ink); }
</style>
</head>
<body>
<main class="stage">
  <article class="business-card">
    <div class="leaf-pattern" role="img" aria-label="Faint pale green leaf pattern"></div>

    <div class="brand">
      <span class="brand-dot"></span>
      <span class="brand-name">Moravel Stenwick</span>
    </div>

    <div class="identity">
      <p class="person-name">Marisa Ortega Bellido BScOT(c)</p>
      <p class="person-role">Occupational Therapist</p>
    </div>

    <ul class="contact">
      <li>
        <svg viewBox="0 0 24 24" aria-hidden="true"><path d="M6.6 10.8a15.1 15.1 0 0 0 6.6 6.6l2.2-2.2a1 1 0 0 1 1-.25 11.4 11.4 0 0 0 3.6.57 1 1 0 0 1 1 1V20a1 1 0 0 1-1 1A17 17 0 0 1 3 4a1 1 0 0 1 1-1h3.5a1 1 0 0 1 1 1c0 1.25.2 2.45.57 3.57a1 1 0 0 1-.25 1z"/></svg>
        <span>(780) 555-0142</span>
      </li>
      <li>
        <svg viewBox="0 0 24 24" aria-hidden="true"><path d="M20 4H4a2 2 0 0 0-2 2v12a2 2 0 0 0 2 2h16a2 2 0 0 0 2-2V6a2 2 0 0 0-2-2zm0 4-8 5-8-5V6l8 5 8-5z"/></svg>
        <span>moravelstenwick@postlynx.net</span>
      </li>
    </ul>
  </article>
</main>
</body>
</html>
```